Business Card Design

New company looking for logo, for business cards and email signature.
we provide Safety, Training and Project Management Services to Mining and Transport sectors.

Industry/Entity Type

Business

Contact Information for Business Card

HOLLOWAY CONSULTANCY, Tom Westcott, Principal Consultant, 0491362284, hollowayconsultancy@examplemail.test , Unit 214,Kestrel Point Trade Centre,581 Tamsin Street, Mackay, 4750.
Sustainable Production through Safety, Training and Leadership.

```html
<!DOCTYPE html>
<html lang="en">
<head>
<meta charset="utf-8">
<title>Holloway Consultancy – Business Card</title>
<link rel="stylesheet" href="https://fonts.googleapis.com/css2?family=Roboto+Condensed:wght@400;700&display=swap">
<style>
  :root {
    --page: #ffffff;
    --card: #ffffff;
    --brand-red: #e31e24;
    --brand-black: #231f20;
    --ink: #1f1f1f;
    --deco-grey: #eceeee;
    --deco-peach: #f9ebe5;
  }
  html, body {
    margin: 0;
    padding: 0;
    width: 1200px;
    height: 1000px;
    overflow: hidden;
    background: var(--page);
    font-family: "Roboto Condensed", "Arial Narrow", sans-serif;
  }
  .card {
    position: absolute;
    left: 208px;
    top: 258px;
    width: 787px;
    height: 485px;
    background: var(--card);
    overflow: hidden;
  }
  .card-frame {
    position: absolute;
    inset: 0;
  }
  .side-pattern {
    position: absolute;
    left: 672px;
    top: 0;
    width: 115px;
    height: 485px;
    background: linear-gradient(180deg, var(--deco-grey) 0%, var(--deco-peach) 25%, var(--deco-grey) 50%, var(--deco-peach) 75%, var(--deco-grey) 100%);
    -webkit-mask-image: linear-gradient(90deg, transparent 0%, #000 55%);
    mask-image: linear-gradient(90deg, transparent 0%, #000 55%);
  }
  .header {
    position: absolute;
    left: 109px;
    top: 46px;
    white-space: nowrap;
  }
  .name {
    color: var(--brand-red);
    font-weight: 700;
    font-size: 38px;
  }
  .role {
    color: var(--ink);
    font-size: 29px;
    margin-left: 8px;
  }
  .services {
    position: absolute;
    left: 112px;
    top: 139px;
    margin: 0;
    padding: 0;
    list-style: none;
    color: var(--ink);
    font-size: 33px;
    line-height: 39px;
  }
  .services li::before {
    content: "\25C6";
    font-size: 17px;
    vertical-align: 5px;
    margin-right: 6px;
  }
  .phone {
    position: absolute;
    left: 109px;
    top: 245px;
    color: var(--brand-red);
    font-size: 48px;
  }
  .email {
    position: absolute;
    left: 109px;
    top: 306px;
    color: var(--ink);
    font-size: 34px;
    white-space: nowrap;
  }
  .address {
    position: absolute;
    left: 109px;
    top: 358px;
    margin: 0;
    color: var(--ink);
    font-size: 29px;
    line-height: 38px;
    font-style: normal;
  }
</style>
</head>
<body>
  <div class="card">
    <svg class="card-frame" width="787" height="485" viewBox="0 0 787 485" aria-hidden="true">
      <rect x="0" y="0" width="30" height="485" fill="var(--brand-black)"/>
      <rect x="30" y="0" width="18" height="485" fill="var(--brand-red)"/>
      <polygon points="48,58 91,101 48,144" fill="var(--brand-red)"/>
      <rect x="91" y="100" width="561" height="2.5" fill="var(--brand-red)"/>
    </svg>
    <div class="side-pattern" role="img" aria-label="Soft grey and peach diamond pattern decoration along the right edge"></div>

    <div class="header">
      <span class="name">Tom Westcott,</span><span class="role">Principal Consultant</span>
    </div>

    <ul class="services">
      <li>Sustainable Production through Safety</li>
      <li>Training and Leadership</li>
    </ul>

    <div class="phone">0491362284</div>
    <div class="email">hollowayconsultancy@examplemail.test</div>
    <address class="address">Unit 214,Kestrel Point Trade Centre<br>581 Tamsin Street, Mackay, 4750.</address>
  </div>
</body>
</html>
```